Bref créative
bluetidal business card
business card for bluetidal.example
Professional
Margaret Pellowin
General Manager
p.o.box 4872 - 519 Maplecrest Ct Nw
garnok77@mailzone.example
http://www.bluetidal.example/
bluetidal logo

```html
<!DOCTYPE html>
<html lang="en">
<head>
<meta charset="utf-8">
<title>bluetidal business card</title>
<link rel="stylesheet" href="https://fonts.googleapis.com/css2?family=Arimo:wght@400;700&display=swap">
<style>
  :root {
    --page-bg: #d6edf4;
    --card-bg: #ffffff;
    --brand-teal: #1ba1c9;
    --wave-light: #8fd3e7;
    --ink-navy: #1f3a6b;
    --on-teal: #ffffff;
  }
  * { margin: 0; padding: 0; box-sizing: border-box; }
  html, body {
    width: 1200px;
    height: 901px;
    overflow: hidden;
    background: var(--page-bg);
    font-family: "Arimo", Arial, sans-serif;
  }
  .business-card {
    position: absolute;
    left: 80px;
    top: 148px;
    width: 1040px;
    height: 604px;
    background: var(--card-bg);
    overflow: hidden;
  }
  .brand-mark {
    position: absolute;
    left: 26px;
    top: 66px;
    display: flex;
    align-items: center;
    gap: 14px;
  }
  .brand-mark__square {
    width: 40px;
    height: 40px;
    background: var(--brand-teal);
  }
  .brand-mark__name {
    font-weight: 700;
    font-size: 54px;
    line-height: 1;
    color: var(--brand-teal);
  }
  .person {
    position: absolute;
    left: 620px;
    top: 84px;
    color: var(--brand-teal);
  }
  .person__name { font-size: 39px; line-height: 1.2; }
  .person__title { font-size: 34px; line-height: 1.3; margin-left: 4px; }
  .contact {
    position: absolute;
    right: 26px;
    top: 238px;
    text-align: right;
    color: var(--ink-navy);
    font-size: 30px;
    line-height: 53px;
    font-style: normal;
  }
  .wave-band {
    position: absolute;
    left: 0;
    top: 426px;
    width: 100%;
    height: 120px;
    background: linear-gradient(to bottom, var(--wave-light), var(--brand-teal));
  }
  .card-footer {
    position: absolute;
    left: 0;
    bottom: 0;
    width: 100%;
    height: 58px;
    background: var(--brand-teal);
    color: var(--on-teal);
    font-size: 30px;
    display: flex;
    justify-content: space-between;
    align-items: center;
    padding: 0 22px 0 12px;
  }
</style>
</head>
<body>
  <main class="business-card">
    <div class="brand-mark">
      <span class="brand-mark__square"></span>
      <span class="brand-mark__name">bluetidal</span>
    </div>

    <div class="person">
      <p class="person__name">Margaret Pellowin</p>
      <p class="person__title">General Manager</p>
    </div>

    <address class="contact">
      <p>p.o.box 4872 - 519 Maplecrest Ct Nw</p>
      <p>Phone: 555-204-7731</p>
      <p>Fax: 555-204-77390</p>
    </address>

    <div class="wave-band" role="img" aria-label="Row of curling ocean waves"></div>

    <footer class="card-footer">
      <span class="card-footer__email">garnok77@mailzone.example</span>
      <span class="card-footer__web">www.bluetidal.example</span>
    </footer>
  </main>
</body>
</html>
```